Packaging design - PROTEIN BALLS

PACKAGING
The packaging is a round carton roll, size: Ø73x180 mm, mockup sample enclosed, The label on the carton roll should have a size of 225x178 mm (width x height)

PRODUCT
Chrunchy, cheesy PROTEIN BALLS (100% pure cheese) with a huge amount of protein (65%), a lot of calcium and very low carbogydrates (3%). Diameter about 1.5 cm.

DESIGN
Since our customers are very sporty people, runner, bodybuilder, etc. The design must fit to this sporty customer segment.

FILES
We need the open data for InDesign with all fonts and pictures. If there are licenses tu buy, we will do it.

SUMMARY
1. SNACK
• Crunchy cheese balls with a diameter of about 1.5cm
• 3 different flavors: "Swiss Alpine Salt", "Provencale" and "Hot Chili"
• High in Protein (65%) and Calcium (2%)
• Low in carbohydrates (3%)

2. PACKAGING
• Carton roll, size: Ø73x180 mm
• Background can be every color, but we think a black one will be high premium.
• Maybe different sports are represented in the background, maybe also cheese
• Be creative
• Label applied, size: 225x178 mm

3. DESIGN
• Product name = (Cheese) PROTEIN BALLS
• 3 different colors for the 3 flavors "Swiss Alpine Salt", "Provencale" and "Hot Chili"
• HighProtein, High Calcium and LowCarb must be pointed out on the front
• Swissness: Swiss made must be pointed out
• fresh and young design, most customers are sporty people, pumper with a strong body awareness

TARGET CUSTOMER
Our main customers are extremely sporty people, who work very hard on their muscles and fitness, most of them are runners, cross fitnesser, bodybuilders, etc We will launch the product in fitness centers, in supplement shops and we are planning to make some stories with sporty influencer.

Serif
Sans Serif

• Cheese, naturalness, healthy, PROTEIN balls, muscles, Swissness must showed on the product.

```html
<!DOCTYPE html>
<html lang="en">
<head>
<meta charset="utf-8">
<title>Cheese Protein Balls – Provencale Label</title>
<link rel="stylesheet" href="https://fonts.googleapis.com/css2?family=Luckiest+Guy&family=Orbitron:wght@700&family=Dancing+Script:wght@700&family=Racing+Sans+One&display=swap">
<style>
  :root {
    --canvas: #ece0b4;
    --label-black: #050607;
    --magenta: #e0187f;
    --violet: #5a3fb0;
    --cheese: #f7c21c;
    --swiss-red: #e12a2d;
    --white: #ffffff;
    --ink: #111111;
  }
  * { margin: 0; padding: 0; box-sizing: border-box; }
  html, body { width: 1200px; height: 1200px; overflow: hidden; }
  body {
    background: var(--canvas);
    display: flex; align-items: center; justify-content: center;
  }
  .label {
    position: relative;
    width: 800px; height: 1133px;
    background: var(--label-black);
    overflow: hidden;
  }
  .label__backdrop {
    position: absolute; inset: 0;
    background:
      linear-gradient(135deg, rgba(224,24,127,.85) 0%, rgba(90,63,176,.55) 22%, transparent 34%),
      linear-gradient(315deg, rgba(224,24,127,.85) 0%, rgba(90,63,176,.55) 20%, transparent 32%);
  }
  .product-title {
    position: absolute; top: 46px; left: 0; width: 100%;
    text-align: center; line-height: 1;
  }
  .product-title__cheese {
    display: block;
    font-family: "Luckiest Guy", sans-serif;
    font-size: 100px;
    color: var(--cheese);
  }
  .product-title__main {
    display: block;
    font-family: "Orbitron", sans-serif; font-weight: 700;
    color: var(--white);
  }
  .product-title__protein { font-size: 62px; margin-top: 4px; letter-spacing: 2px; }
  .product-title__balls { font-size: 84px; margin-top: 6px; letter-spacing: 6px; }
  .swiss-badge {
    position: absolute; top: 312px; left: 278px;
    width: 244px; height: 44px;
    background: var(--swiss-red);
    display: flex; align-items: center; justify-content: center;
    color: var(--white);
    font-family: "Racing Sans One", sans-serif;
    font-size: 24px; letter-spacing: 1px;
  }
  .hero-artwork {
    position: absolute; top: 380px; left: 150px;
    width: 500px; height: 540px;
    border-radius: 48%;
    background: radial-gradient(circle at 50% 50%, #f3d77a 0 22%, #b47a4e 42%, #3d5aa8 62%, transparent 72%);
  }
  .flavour-name {
    position: absolute; top: 934px; left: 0; width: 100%;
    text-align: center;
    font-family: "Orbitron", sans-serif; font-weight: 700;
    font-size: 46px; line-height: 1; letter-spacing: 1px;
    color: var(--white);
  }
  .flavour-word {
    position: absolute; top: 982px; left: 0; width: 100%;
    text-align: center;
    font-family: "Dancing Script", cursive;
    font-size: 40px; line-height: 1;
    color: var(--swiss-red);
  }
  .claims-bar {
    position: absolute; top: 1045px; left: 127px;
    width: 546px; height: 48px;
    background: var(--white);
    display: flex; align-items: center; justify-content: center; gap: 14px;
    font-family: "Racing Sans One", sans-serif;
    font-size: 21px; color: var(--ink); letter-spacing: .5px;
  }
  .claims-bar__divider { color: var(--swiss-red); }
</style>
</head>
<body>
  <main class="label">
    <div class="label__backdrop" role="img" aria-label="Diagonal pink and violet sport stripes with thin line accents in the top-left and bottom-right corners"></div>

    <h1 class="product-title">
      <span class="product-title__cheese">CHEESE</span>
      <span class="product-title__main product-title__protein">PROTEIN</span>
      <span class="product-title__main product-title__balls">BALLS</span>
    </h1>

    <div class="swiss-badge">SWISS MADE</div>

    <div class="hero-artwork" role="img" aria-label="Colourful watercolour athletes – karate fighters, volleyball, basketball, cyclist, hurdler, runner, tennis and football players, bodybuilder – circling cheese blocks and three protein balls"></div>

    <div class="flavour-name">PROVECALE</div>
    <div class="flavour-word">flavour</div>

    <div class="claims-bar">
      <span>HIGH PROTEIN</span><span class="claims-bar__divider">/</span>
      <span>HIGH CALCIUM</span><span class="claims-bar__divider">/</span>
      <span>LOW CARB</span>
    </div>
  </main>
</body>
</html>
```